Dale Morrikan Plumbing and Heating

Need a card design for a plumbing and heating company that does service and repair, remodels, and plumbing in new construction. Please add following on back side of card; Boilers, Water heaters, Gas lines, Sump pumps, Toilet repairs, Faucet repairs, Pipe thawing, Radiant heating, New construction, Remodels.

Industry/Entity Type

Plumber

Contact Information for Business Card

Was thinking white gloss card with colored logo in middle or black glossy card with silver logo in middle. Just a thought but very open to other designs.

Requirements
Must have
• Need following on front of card;
• P(203) 321-8689
• C(203) 232-9069
• Dale Morrikan 275 Larkwell St West, Stamford, Ct 06214
• service@DrainHearth.example (plumbing in blue, heating in red)
• www.DrainHearth.example (plumbing in blue, heating in red)
• Fully Licensed and Insured
Nice to have
• Elegant design

```html
<!DOCTYPE html>
<html lang="en">
<head>
<meta charset="utf-8">
<title>Dale Morrikan Plumbing and Heating – Business Card</title>
<link rel="stylesheet" href="https://fonts.googleapis.com/css2?family=Michroma&family=Exo+2:wght@300;400&family=Ubuntu:wght@500;700&display=swap">
<style>
  :root {
    --canvas: #eeeeee;
    --card: #000000;
    --silver: #cfcfcf;
    --white: #ffffff;
    --blue: #1f6fd6;
    --red: #e0322b;
    --drop: #4aa3f0;
    --faint: #2a2a2a;
  }
  * { margin: 0; padding: 0; box-sizing: border-box; }
  html, body { width: 988px; height: 1200px; overflow: hidden; background: var(--canvas); }
  .canvas { position: relative; width: 988px; height: 1200px; }

  .card {
    position: absolute; left: 90px; width: 788px; height: 467px;
    background: var(--card); color: var(--white); overflow: hidden;
    font-family: "Ubuntu", sans-serif;
  }
  .card--front { top: 97px; }
  .card--back { top: 635px; }

  .center-line { position: absolute; left: 0; right: 0; text-align: center; white-space: nowrap; }

  /* front */
  .brand-mark {
    position: absolute; left: 344px; top: 40px; width: 100px; height: 100px;
    border-radius: 50%; border: 6px solid var(--silver);
  }
  .brand-name {
    top: 170px; font-family: "Michroma", sans-serif; color: var(--silver);
    font-size: 29px; letter-spacing: 1px; line-height: 36px;
  }
  .brand-trade {
    top: 207px; font-family: "Michroma", sans-serif; color: var(--silver);
    font-size: 19px; letter-spacing: 2.5px; line-height: 24px;
  }
  .rule-row {
    position: absolute; left: 0; right: 0; display: flex; align-items: center; gap: 12px;
  }
  .rule { flex: 1; height: 2px; background: linear-gradient(90deg, transparent, var(--silver)); }
  .rule--right { background: linear-gradient(90deg, var(--silver), transparent); }
  .web { font-weight: 700; font-size: 21px; letter-spacing: 0.5px; white-space: nowrap; }
  .tone-blue { color: var(--blue); }
  .tone-red { color: var(--red); }

  .front-web { top: 248px; }
  .person { top: 298px; font-weight: 700; font-size: 24px; }
  .phones {
    top: 340px; font-family: "Exo 2", sans-serif; font-weight: 300; font-size: 29px;
    display: flex; justify-content: center; gap: 46px;
  }
  .phone { display: inline-flex; align-items: center; gap: 6px; }
  .phone svg { width: 22px; height: 26px; }
  .email {
    top: 397px; font-weight: 700; font-size: 21px;
    display: flex; justify-content: center; align-items: center; gap: 8px;
  }
  .email svg { width: 26px; height: 18px; }

  /* back */
  .faint-name {
    position: absolute; right: -30px; top: 70px; font-family: "Michroma", sans-serif;
    font-size: 56px; color: var(--faint); white-space: nowrap;
  }
  .licence-row { top: 54px; left: 160px; right: 190px; }
  .licence { font-weight: 700; font-size: 26px; white-space: nowrap; }
  .licence-rule { position: absolute; left: 165px; width: 380px; top: 97px; height: 2px;
    background: linear-gradient(90deg, transparent, var(--silver), transparent); }
  .services {
    position: absolute; top: 125px; left: 0; width: 788px;
    display: grid; grid-template-columns: 357px 22px auto; row-gap: 7px;
    font-weight: 700; font-size: 24px; line-height: 36px; letter-spacing: 0.3px;
  }
  .service--left { text-align: right; padding-right: 2px; }
  .service--right { padding-left: 4px; }
  .drop { display: flex; align-items: center; justify-content: center; }
  .drop svg { width: 14px; height: 19px; }
  .back-web { top: 385px; }
</style>
</head>
<body>
<main class="canvas">

  <section class="card card--front">
    <div class="brand-mark" aria-hidden="true"></div>
    <div class="center-line brand-name">DALE MORRIKAN</div>
    <div class="center-line brand-trade">PLUMBING AND HEATING</div>

    <div class="rule-row front-web">
      <span class="rule"></span>
      <span class="web">www.<span class="tone-blue">Drain</span><span class="tone-red">Hearth</span>.example</span>
      <span class="rule rule--right"></span>
    </div>

    <div class="center-line person">Dale Morrikan</div>
    <div class="center-line phones">
      <span class="phone">
        <svg viewBox="0 0 22 26" aria-label="Phone"><path d="M5 2 L9 2 L10 8 L7 10 Q9 16 14 19 L16 16 L21 18 L20 23 Q12 25 6 16 Q2 9 5 2 Z" fill="none" stroke="#fff" stroke-width="2"/></svg>
        (203) 555-0147
      </span>
      <span class="phone">
        <svg viewBox="0 0 22 26" aria-label="Mobile"><rect x="4" y="2" width="14" height="22" rx="2" fill="none" stroke="#fff" stroke-width="2"/><line x1="9" y1="20" x2="13" y2="20" stroke="#fff" stroke-width="2"/></svg>
        (203) 555-0183
      </span>
    </div>
    <div class="center-line email">
      <svg viewBox="0 0 26 18" aria-label="Email"><rect x="1" y="1" width="24" height="16" fill="none" stroke="#fff" stroke-width="2"/><path d="M1 1 L13 10 L25 1" fill="none" stroke="#fff" stroke-width="2"/></svg>
      <span>service@<span class="tone-blue">Drain</span><span class="tone-red">Hearth</span>.example</span>
    </div>
  </section>

  <section class="card card--back">
    <div class="faint-name" aria-hidden="true">Dale Morrikan</div>
    <div class="center-line licence" style="top:54px; left:-20px;">Fully Licensed and Insured</div>
    <div class="licence-rule"></div>

    <div class="services">
      <span class="service--left">Boilers</span><span class="drop"><svg viewBox="0 0 14 19"><path d="M7 0 Q14 10 13 13 A6 6 0 0 1 1 13 Q0 10 7 0 Z" fill="var(--drop)"/></svg></span><span class="service--right">Faucet repairs</span>
      <span class="service--left">Water heaters</span><span class="drop"><svg viewBox="0 0 14 19"><path d="M7 0 Q14 10 13 13 A6 6 0 0 1 1 13 Q0 10 7 0 Z" fill="var(--drop)"/></svg></span><span class="service--right">Pipe thawing</span>
      <span class="service--left">Gas lines</span><span class="drop"><svg viewBox="0 0 14 19"><path d="M7 0 Q14 10 13 13 A6 6 0 0 1 1 13 Q0 10 7 0 Z" fill="var(--drop)"/></svg></span><span class="service--right">Radiant heating</span>
      <span class="service--left">Sump pumps</span><span class="drop"><svg viewBox="0 0 14 19"><path d="M7 0 Q14 10 13 13 A6 6 0 0 1 1 13 Q0 10 7 0 Z" fill="var(--drop)"/></svg></span><span class="service--right">New construction</span>
      <span class="service--left">Toilet repairs</span><span class="drop"><svg viewBox="0 0 14 19"><path d="M7 0 Q14 10 13 13 A6 6 0 0 1 1 13 Q0 10 7 0 Z" fill="var(--drop)"/></svg></span><span class="service--right">Remodels</span>
    </div>

    <div class="rule-row back-web">
      <span class="rule"></span>
      <span class="web">www.<span class="tone-blue">Drain</span><span class="tone-red">Hearth</span>.example</span>
      <span class="rule rule--right"></span>
    </div>
  </section>

</main>
</body>
</html>
```